Web Design Project

We need a web site design for a new company based in New York/New Jersey called "The Lumenfold Group". We develop innovative strategies for marketing, strategic planning, business development, public relations in economic development. Simply put we create innovative strategies for invigorating smarter and stronger leaders and companies. We are a consulting firm with bold ideas for affecting change. We want to communicate that partnering with The Lumenfold Group your first decision to breakthrough innovation.

Target Market(s)

The target audience for the consulting services are private companies, economic development organizations, government and other interested in community investment strategies globally.

Industry/Entity Type

Business

Font styles to use
Serif
Sans Serif

Requirements
Must have
Nice to have
Should not have

```html
<!DOCTYPE html>
<html lang="en">
<head>
<meta charset="utf-8">
<title>The Lumenfold Group</title>
<link rel="stylesheet" href="https://fonts.googleapis.com/css2?family=Roboto+Condensed:wght@400;700&family=Open+Sans:ital,wght@0,400;0,600;1,400&display=swap">
<style>
:root{
  --blue:#4197d3;
  --blue-dark:#2f86c4;
  --ink:#333333;
  --muted:#6a6a6a;
  --line:#dcdcdc;
  --nav:#6f7378;
  --band:#f4f4f4;
  --footer:#2b2b2b;
  --white:#ffffff;
}
*{margin:0;padding:0;box-sizing:border-box}
html,body{width:758px;height:1200px;overflow:hidden;background:var(--white)}
body{position:relative;font-family:"Open Sans",Arial,sans-serif;color:var(--ink)}
.abs{position:absolute}
.cond{font-family:"Roboto Condensed","Arial Narrow",sans-serif}

.brand{left:82px;top:22px;font-size:21px;color:#5d6166;letter-spacing:-.2px}
.brand b{font-weight:400;color:var(--blue)}
.lang{left:591px;top:21px;width:85px;height:23px;border:1px solid #cfcfcf;font-size:8px;color:#777;display:flex;align-items:center;padding-left:8px;gap:6px}
.lang .flag{width:11px;height:8px;background:#3c4f86;border:1px solid #d8d8d8}
.lang .caret{margin-left:auto;margin-right:9px;width:0;height:0;border-left:3px solid transparent;border-right:3px solid transparent;border-top:3px solid #888}

.nav{left:82px;top:69px;width:594px;height:33px;background:var(--nav);display:flex;font-size:8.6px;color:var(--white);text-transform:uppercase}
.nav a{color:inherit;text-decoration:none;display:flex;align-items:center;padding:0 20px 0 20px;height:100%}
.nav a.active{background:var(--blue);width:66px;justify-content:center;padding:0}

.hero{left:0;top:102px;width:758px;height:304px;background:linear-gradient(90deg,#c9d3db 0%,#dfe5ea 30%,#b9c0c6 55%,#4c545e 72%,#6c7682 90%,#d8dde2 96%)}
.cap{background:rgba(70,72,76,.82);color:var(--white)}
.cap-title{left:113px;top:209px;width:209px;height:29px;font-size:20px;font-weight:700;display:flex;align-items:center;padding-left:12px}
.cap-line{height:22px;font-size:9px;display:flex;align-items:center;padding-left:11px}
.cap-1{left:113px;top:255px;width:291px}
.cap-2{left:113px;top:285px;width:245px}
.arrow{top:249px}

.feature{top:466px;width:181px;height:93px;border:1px solid var(--line);text-align:center}
.feature h3{position:absolute;top:34px;width:100%;font-size:11.5px;font-weight:400;color:var(--blue-dark)}
.feature p{position:absolute;top:56px;width:100%;font-size:7.8px;line-height:12.5px;color:var(--muted)}
.badge{top:440px;width:50px;height:50px;border-radius:50%;border:1px solid var(--line);background:var(--white);display:flex;align-items:center;justify-content:center}
.badge.on{background:var(--blue);border-color:var(--blue)}

.h2{width:758px;text-align:center;font-size:16px;color:var(--ink)}
.h2 span{color:var(--blue)}
.welcome-text{left:106px;top:628px;width:546px;text-align:center;font-size:7.9px;line-height:17.2px;color:var(--muted)}
.btn-blue{left:343px;top:692px;width:72px;height:25px;background:var(--blue);color:var(--white);font-size:8.4px;display:flex;align-items:center;justify-content:center}

.news-band{left:0;top:746px;width:758px;height:226px;background:var(--band)}
.news-photo{width:116px;height:77px;background:linear-gradient(135deg,#eef1f3,#d7dce0 55%,#bfc5cb)}
.news-text{width:150px;font-size:7.9px;line-height:15.3px;color:var(--muted)}
.news-text .date{color:var(--blue-dark);margin-bottom:5px}
.news-text .more{color:var(--blue-dark);margin-top:5px}
.btn-ghost{left:342px;top:920px;width:74px;height:25px;border:1.5px solid #cfcfcf;color:#777;font-size:8px;display:flex;align-items:center;justify-content:center;background:var(--white)}

.partner{top:1034px;width:83px;height:50px;border:1px solid var(--line);display:flex;align-items:center;justify-content:center}
.partner i{display:block;width:26px;height:26px;background:#d9dde0}

.footer{left:0;top:1115px;width:758px;height:85px;background:var(--footer)}
.social{top:1137px;width:20px;height:20px;border-radius:50%;border:1.5px solid #9a9a9a;background:#3b3b3b}
.copy{left:84px;top:1176px;font-size:7.5px;color:#9a9a9a}
.nl-title{left:522px;top:1134px;font-size:10.5px;color:#e6e6e6}
.nl-input{left:521px;top:1160px;width:150px;height:19px;background:#f0f0f0;display:flex;align-items:center}
.nl-input span{flex:1;padding-left:10px;font-size:7px;font-style:italic;color:#999}
.nl-input .go{width:22px;height:100%;border-left:1px solid #d0d0d0;display:flex;align-items:center;justify-content:center}
</style>
</head>
<body>

<header>
  <div class="abs brand cond">The <b>Lumenfold</b> Group</div>
  <div class="abs lang"><span class="flag"></span>English<span class="caret"></span></div>
  <nav class="abs nav">
    <a class="active" href="#">Home</a>
    <a href="#">About Us</a>
    <a href="#">Services</a>
    <a href="#">News</a>
    <a href="#">Testimonials</a>
    <a href="#">Contact Us</a>
  </nav>
</header>

<section>
  <div class="abs hero" role="img" aria-label="Photo of a smiling businessman in a suit standing in a bright office"></div>
  <h1 class="abs cap cap-title cond">Neque porro dolorem</h1>
  <div class="abs cap cap-line cap-1 cond">Lorem ipsum dolor sit amet, consectetur adipiscing elit, sed do eius</div>
  <div class="abs cap cap-line cap-2 cond">mod tempor incididunt ut labore et dolore magna aliqua.</div>
  <svg class="abs arrow" style="left:68px" width="28" height="28" viewBox="0 0 28 28"><circle cx="14" cy="14" r="12.5" fill="rgba(255,255,255,.25)" stroke="#fff" stroke-width="1.5"/><path d="M16 8 L10 14 L16 20" fill="none" stroke="#fff" stroke-width="2.5"/></svg>
  <svg class="abs arrow" style="left:664px" width="28" height="28" viewBox="0 0 28 28"><circle cx="14" cy="14" r="12.5" fill="rgba(255,255,255,.25)" stroke="#fff" stroke-width="1.5"/><path d="M12 8 L18 14 L12 20" fill="none" stroke="#fff" stroke-width="2.5"/></svg>
</section>

<section>
  <div class="abs feature" style="left:83px"><h3 class="cond">Strategies for marketing</h3><p>Lorem ipsum dolor sit amet, consect<br>etur adipiscing elit aliqua.</p></div>
  <div class="abs feature" style="left:289px"><h3 class="cond">Strategic planning</h3><p>Lorem ipsum dolor sit amet, consect<br>etur adipiscing elit aliqua.</p></div>
  <div class="abs feature" style="left:494px"><h3 class="cond">Business development</h3><p>Lorem ipsum dolor sit amet, consect<br>etur adipiscing elit aliqua.</p></div>

  <div class="abs badge on" style="left:151px">
    <svg width="18" height="18" viewBox="0 0 18 18" fill="none" stroke="#fff" stroke-width="1.4"><rect x="2" y="3" width="14" height="10"/><path d="M4 11 L7 8 L9 10 L13 6"/><path d="M9 13 V16 M6 16 H12"/></svg>
  </div>
  <div class="abs badge" style="left:354px">
    <svg width="16" height="18" viewBox="0 0 16 18" fill="none" stroke="#666" stroke-width="1.3"><rect x="2" y="1" width="12" height="16"/><rect x="4" y="3" width="8" height="3"/><path d="M4 9H6M7 9H9M10 9H12M4 12H6M7 12H9M10 12H12M4 15H6M7 15H9M10 15H12"/></svg>
  </div>
  <div class="abs badge" style="left:556px">
    <svg width="18" height="16" viewBox="0 0 18 16"><rect x="1" y="1" width="16" height="14" fill="#555"/><text x="5" y="12" font-family="Open Sans,sans-serif" font-size="10" font-weight="700" fill="#fff" text-anchor="middle">$</text><path d="M10 5H15M10 8H15M10 11H15" stroke="#fff" stroke-width="1.3"/></svg>
  </div>
</section>

<section>
  <h2 class="abs h2 cond" style="left:0;top:595px;font-weight:400">Welcome to Our Website <span>Mainpage</span></h2>
  <p class="abs welcome-text">Lorem ipsum dolor sit amet, consectetur adipiscing elit, sed do eiusmod tempor incididunt ut labore et dolore magna aliqua. Ut enim ad minim veniam, quis nostrud exercitation ullamco laboris nisi ut aliquip ex ea commodo consequat. Lorem ipsum dolor sit amet, consectetur adipiscing elit, sed do eiusmod tempor incididunt ut labore et dolore magna aliqua.</p>
  <a class="abs btn-blue">Learn More</a>
</section>

<section>
  <div class="abs news-band"></div>
  <h2 class="abs h2 cond" style="left:0;top:767px;font-weight:400">Latest <span>News</span></h2>

  <div class="abs news-photo" style="left:82px;top:809px" role="img" aria-label="Photo of a businesswoman with colleagues in an office"></div>
  <div class="abs news-text" style="left:216px;top:811px">
    <div class="date">18/Sept/2014</div>
    Lorem ipsum dolor sit amet, consect etur adipiscing elit, sed do eiusmod tempor incididunt aliqua.
    <div class="more">Continue Reading &gt;&gt;</div>
  </div>

  <div class="abs news-photo" style="left:397px;top:810px;width:114px;background:linear-gradient(135deg,#e4e6e8,#a9aeb3 50%,#eceeef)" role="img" aria-label="Photo of business people meeting at a table"></div>
  <div class="abs news-text" style="left:529px;top:809px">
    <div class="date">18/Sept/2014</div>
    Lorem ipsum dolor sit amet, consect etur adipiscing elit, sed do eiusmod tempor incididunt aliqua.
    <div class="more">Continue Reading &gt;&gt;</div>
  </div>

  <a class="abs btn-ghost">Learn More</a>
</section>

<section>
  <h2 class="abs h2 cond" style="left:0;top:999px;font-weight:400">Our <span>Partners</span></h2>
  <div class="abs partner" style="left:83px"><i style="background:#f0a36f"></i></div>
  <div class="abs partner" style="left:185px"><i style="background:#8cc3d6"></i></div>
  <div class="abs partner" style="left:287px"><i style="background:#c8b58f;border-radius:50%"></i></div>
  <div class="abs partner" style="left:390px"><i style="background:#d8e07a;border-radius:50%"></i></div>
  <div class="abs partner" style="left:491px"><i style="background:#f2a04a;border-radius:50%"></i></div>
  <div class="abs partner" style="left:594px"><i style="background:#6aa9d8"></i></div>
</section>

<footer>
  <div class="abs footer"></div>
  <span class="abs social" style="left:84px"></span>
  <span class="abs social" style="left:110px"></span>
  <span class="abs social" style="left:136px"></span>
  <span class="abs social" style="left:163px"></span>
  <p class="abs copy">©2014. Yoursite. All right reserved.</p>
  <div class="abs nl-title">Newsletter SignUp</div>
  <div class="abs nl-input"><span>Enter your Email...</span><div class="go"><svg width="6" height="8" viewBox="0 0 6 8"><path d="M1 1 L5 4 L1 7" fill="none" stroke="#777" stroke-width="1.4"/></svg></div></div>
</footer>

</body>
</html>
```